Flyer for Pharmacy/Medical Convention

Tri-fold flyer for pharmacy/medical convention. The inside of the flyer we would like to look like a venn diagram, possibly using an image similar to our blue logo

Copy write will be submitted when a design is chosen

there will be a flap about educational features, one about supplements an automated recommendations, and a flap about a computer platform to manage patients

Target Market(s)

Pharmacists and Medical Providers

Industry/Entity Type

Supplement

Colors

Designer to choose colors to be used in the design.

Requirements
Must have
• color scheme similar to logos and or label design attached

```html
<!DOCTYPE html>
<html lang="en">
<head>
<meta charset="utf-8">
<title>Veralis Wellness Solutions – Brochure Outside</title>
<link href="https://fonts.googleapis.com/css2?family=Montserrat:wght@400;500;700;800&display=swap" rel="stylesheet">
<style>
  :root{
    --stage:#3b3b3d;
    --navy:#283891;
    --navy-deep:#1c2a78;
    --navy-soft:#5668bd;
    --red:#e0262a;
    --orange:#f05a24;
    --silver:#d9dadf;
    --ink:#1d1d1f;
    --white:#ffffff;
    --globe:#aab3e0;
  }
  *{box-sizing:border-box;margin:0;padding:0}
  html,body{width:817px;height:1200px;overflow:hidden;background:var(--stage)}
  body{font-family:"Montserrat",Arial,sans-serif;position:relative}
  .brochure{position:absolute;left:20px;top:298px;width:777px;height:601px;background:var(--white);overflow:hidden;box-shadow:0 6px 20px rgba(0,0,0,.45)}
  .brochure__shapes{position:absolute;inset:0}
  .abs{position:absolute}

  .about__title{left:27px;top:54px;font-size:19px;font-weight:800;color:var(--navy-soft);letter-spacing:.3px}
  .about__body{left:27px;top:84px;width:212px;color:var(--white);font-size:8.2px;line-height:11px;text-align:justify}
  .about__body p{margin-bottom:7px}
  .about__list{left:27px;top:290px;width:212px;list-style:none;color:var(--white);font-size:8.2px;line-height:11px}
  .about__list li{position:relative;padding-left:24px;margin-bottom:8px}
  .about__list li::before{content:attr(data-n);position:absolute;left:0;top:0;width:13px;height:13px;border-radius:50%;background:var(--red);font-size:7.5px;font-weight:700;text-align:center;line-height:13px}

  .intro{left:272px;top:116px;width:210px;text-align:center}
  .intro__title{color:var(--red);font-size:22px;font-weight:800;line-height:27px}
  .intro__text{margin-top:4px;color:var(--ink);font-size:11.5px;line-height:16px}

  .brand{font-weight:700;letter-spacing:.3px}
  .brand--top{left:572px;top:34px;width:196px;text-align:center;color:var(--navy);font-size:16px;line-height:20px}
  .brand--contact{left:258px;top:488px;width:240px;text-align:center;color:var(--white);font-size:13px;line-height:17px}

  .contact{left:258px;top:522px;width:240px;text-align:center;color:var(--white);font-size:8.6px;line-height:13.5px}
  .contact__lead{font-weight:700}
  .contact__icons{display:flex;justify-content:center;gap:6px;margin:3px 0 2px}

  .headline{left:520px;top:450px;width:250px;text-align:center;color:var(--white)}
  .headline__top{font-size:22px;font-weight:500;line-height:26px}
  .headline__main{font-size:30px;font-weight:800;color:var(--red);line-height:32px}
  .headline__text{margin-top:6px;font-size:8.6px;line-height:12px}
  .headline__icon{left:636px;top:552px}
  .headline__web{left:520px;top:576px;width:250px;text-align:center;color:var(--white);font-size:8.6px}
</style>
</head>
<body>
<main class="brochure">
  <svg class="brochure__shapes" viewBox="0 0 777 601" width="777" height="601">
    <defs>
      <linearGradient id="silverBand" x1="0" y1="0" x2="0" y2="1">
        <stop offset="0" stop-color="#c9cbd1"/><stop offset="1" stop-color="#f3f4f6"/>
      </linearGradient>
      <linearGradient id="staffPhoto" x1="0" y1="0" x2="1" y2="1">
        <stop offset="0" stop-color="#eef3f8"/><stop offset=".5" stop-color="#d8e3ee"/><stop offset="1" stop-color="#f3efe9"/>
      </linearGradient>
      <linearGradient id="productPhoto" x1="0" y1="0" x2="0" y2="1">
        <stop offset="0" stop-color="#f4f5f8"/><stop offset="1" stop-color="#dfe3ec"/>
      </linearGradient>
      <linearGradient id="deskPhoto" x1="0" y1="0" x2="1" y2="1">
        <stop offset="0" stop-color="#c7d3dc"/><stop offset="1" stop-color="#eef1f3"/>
      </linearGradient>
      <linearGradient id="navyFill" x1="0" y1="0" x2="1" y2="1">
        <stop offset="0" stop-color="#2f40a0"/><stop offset="1" stop-color="#1e2c7c"/>
      </linearGradient>
      <clipPath id="leftPanel"><rect x="0" y="0" width="250" height="601"/></clipPath>
    </defs>

    <rect x="0" y="0" width="777" height="150" fill="url(#silverBand)"/>
    <rect role="img" aria-label="Photo: two smiling pharmacists in white coats in a pharmacy" x="484" y="110" width="293" height="340" fill="url(#staffPhoto)"/>
    <path d="M250 40 C450 40 620 110 777 142 L777 160 C660 132 570 122 484 126 L484 450 L250 450 Z" fill="#ffffff"/>
    <rect role="img" aria-label="Photo: four supplement bottles" x="278" y="262" width="206" height="148" rx="6" fill="url(#productPhoto)"/>
    <path d="M250 30 C450 30 620 100 777 132 L777 146 C620 114 450 44 250 44 Z" fill="var(--navy)"/>

    <path d="M0 24 C90 20 180 22 260 28 L260 601 L0 601 Z" fill="url(#navyFill)"/>
    <g clip-path="url(#leftPanel)">
      <circle cx="134" cy="552" r="138" fill="#ffffff"/>
      <path d="M14 484 A138 138 0 0 1 250 478" fill="none" stroke="var(--red)" stroke-width="7"/>
      <circle role="img" aria-label="Photo: stethoscope resting on a medical form" cx="134" cy="552" r="128" fill="url(#deskPhoto)"/>
    </g>
    <line x1="250" y1="30" x2="250" y2="601" stroke="#ffffff" stroke-width="6"/>

    <path d="M253 450 C420 450 600 430 777 392 L777 601 L253 601 Z" fill="url(#navyFill)"/>
    <path d="M253 446 C420 446 600 426 777 386" fill="none" stroke="var(--orange)" stroke-width="4"/>
    <path d="M437 448 C580 438 690 420 777 400" fill="none" stroke="var(--red)" stroke-width="9"/>
  </svg>

  <h2 class="abs about__title">ABOUT US</h2>
  <div class="abs about__body">
    <p>Recognizing a need for a line of nutritional supplements designed by health care professionals, Veralis Wellness Solutions was created. Of utmost importance to the health professionals and patients served by Veralis Wellness Solutions is quality ingredients, efficacious doses, and company integrity.</p>
    <p>Veralis Wellness Solutions remains committed to a Science Based approach and philosophy. Our products are developed utilizing research from evidence-based, peer reviewed journals and nutritionally minded healthcare providers.</p>
    <p>Veralis Wellness Solutions delivers only highly effective, professional grade supplements. To achieve these goals, VWS adheres to these standards:</p>
  </div>
  <ol class="abs about__list">
    <li data-n="1">Research-based formulas at therapeutic dosages</li>
    <li data-n="2">Quality-Assured raw material ingredients (tested for potency and contaminants)</li>
    <li data-n="3">Manufactured in facilities that are fully compliant with current Good Manufacturing Practices (cGMP's), FDA, NSF, TGA, NPA</li>
  </ol>

  <div class="abs brand brand--top">Veralis Wellness Solutions</div>

  <div class="abs intro">
    <h1 class="intro__title">VERALIS<br>WELLNESS</h1>
    <p class="intro__text">Solutions strives to be an ethical partner for healthcare providers and patients.</p>
  </div>

  <div class="abs brand brand--contact">Veralis Wellness Solutions</div>
  <div class="abs contact">
    <p class="contact__lead">Get in touch with us</p>
    <div class="contact__icons">
      <svg width="13" height="10" viewBox="0 0 13 10"><rect x=".5" y=".5" width="12" height="9" fill="none" stroke="#fff"/><path d="M.5 .5 L6.5 5.5 L12.5 .5" fill="none" stroke="#fff"/></svg>
      <svg width="11" height="11" viewBox="0 0 11 11"><circle cx="5.5" cy="5.5" r="5" fill="none" stroke="#fff"/><ellipse cx="5.5" cy="5.5" rx="2.2" ry="5" fill="none" stroke="#fff"/><line x1=".5" y1="5.5" x2="10.5" y2="5.5" stroke="#fff"/></svg>
    </div>
    <p>info@veraliswellness.com</p>
    <p>www.veraliswellness.com</p>
  </div>

  <div class="abs headline">
    <p class="headline__top">Headline Text</p>
    <p class="headline__main">GOES HERE</p>
    <p class="headline__text">Lorem Ipsum is simply dummy text of the printing and typesetting industry.</p>
  </div>
  <svg class="abs headline__icon" width="18" height="18" viewBox="0 0 18 18"><circle cx="9" cy="9" r="8" fill="none" stroke="var(--globe)"/><ellipse cx="9" cy="9" rx="3.6" ry="8" fill="none" stroke="var(--globe)"/><line x1="1" y1="9" x2="17" y2="9" stroke="var(--globe)"/></svg>
  <p class="abs headline__web">www.veraliswellness.com</p>
</main>
</body>
</html>
```